Need a webinar banner promo to place on social media

We are organise a series of webinars in coming months.

We need a webinar banner design to be posted on Facebook and linkedin. The banner is for our webinar titled: Ways to Debut a Novel with Sparkle and Flair.

our website is www.quillmarket.com.au

there is a link on the website to the webinar registration for your reference.

```html
<!DOCTYPE html>
<html lang="en">
<head>
<meta charset="utf-8">
<title>Free Webinar – Ways to Debut a Novel with Sparkle and Flair</title>
<link href="https://fonts.googleapis.com/css2?family=Archivo+Black&family=Barlow+Condensed:wght@400;500&family=Barlow+Semi+Condensed:wght@400&family=Arimo:wght@400;700&display=swap" rel="stylesheet">
<style>
  :root {
    --navy: #0b2240;
    --band: #1f2a3a;
    --gold: #b38430;
    --gold-light: #e3c865;
    --cream-a: #f8eec2;
    --cream-b: #fdf9ec;
    --ink: #111111;
    --white: #ffffff;
  }
  * { margin: 0; padding: 0; box-sizing: border-box; }
  html, body {
    width: 1200px; height: 1034px; overflow: hidden; background: var(--white);
  }
  .canvas { position: relative; width: 1200px; height: 1034px; }
  .banner {
    position: absolute; left: 38px; top: 142px; width: 1124px; height: 749px;
    background: linear-gradient(120deg, var(--cream-a) 0%, var(--cream-b) 55%, var(--cream-a) 100%);
    overflow: hidden;
  }
  .shapes { position: absolute; inset: 0; }
  .live-badge {
    position: absolute; left: 62px; top: 35px; height: 42px; display: flex; align-items: center;
  }
  .live-badge .pill {
    position: relative; z-index: 2; display: flex; align-items: center; gap: 6px;
    height: 42px; padding: 0 14px 0 2px; background: var(--gold); border-radius: 21px;
    font-family: "Archivo Black", sans-serif; color: var(--white); font-size: 28px; letter-spacing: 0.5px;
    white-space: nowrap;
  }
  .live-badge .play { width: 40px; height: 40px; }
  .live-badge .label {
    margin-left: -14px; height: 42px; width: 262px; padding-left: 28px; background: var(--navy);
    color: var(--white); font-family: "Arimo", sans-serif; font-size: 29px; line-height: 42px;
    white-space: nowrap; overflow: hidden;
  }
  .title {
    position: absolute; left: 60px; top: 112px; width: 520px;
    font-family: "Archivo Black", sans-serif; font-size: 50px; line-height: 56px;
    color: var(--navy); text-transform: uppercase; letter-spacing: 0.5px;
  }
  .schedule {
    position: absolute; left: 60px; top: 352px;
    font-family: "Barlow Condensed", sans-serif; font-weight: 400; font-size: 48px; line-height: 54px; color: var(--ink);
  }
  .pitch {
    position: absolute; left: 60px; top: 465px; width: 380px;
    font-family: "Barlow Semi Condensed", sans-serif; font-size: 17px; line-height: 21px; color: var(--ink);
  }
  .pitch p + p { margin-top: 15px; }
  .register-band {
    position: absolute; left: 0; top: 611px; width: 470px; height: 37px; background: var(--band);
    color: var(--white); font-family: "Barlow Condensed", sans-serif; font-size: 24px; line-height: 37px; padding-left: 60px;
  }
  .register-url {
    position: absolute; left: 60px; top: 660px;
    font-family: "Barlow Semi Condensed", sans-serif; font-size: 23px; color: var(--ink);
  }
  .brand {
    position: absolute; z-index: 3; left: 920px; top: 62px; width: 160px; text-align: center;
    font-family: "Barlow Condensed", sans-serif; font-weight: 500; font-size: 38px; line-height: 38px; color: var(--gold);
    letter-spacing: 1px;
  }
  .event-photo {
    position: absolute; left: 626px; top: 163px; width: 348px; height: 348px; border-radius: 50%;
    background: radial-gradient(circle at 50% 55%, #c9504a 0%, #8a3d5a 30%, #2b3f6b 62%, #141a28 100%);
  }
</style>
</head>
<body>
<div class="canvas">
  <section class="banner">
    <svg class="shapes" width="1124" height="749" viewBox="0 0 1124 749" aria-hidden="true">
      <defs>
        <linearGradient id="ring" x1="0" y1="0" x2="1" y2="1">
          <stop offset="0" stop-color="#c9a040"/>
          <stop offset="0.35" stop-color="#e9d677"/>
          <stop offset="0.7" stop-color="#c9a040"/>
          <stop offset="1" stop-color="#9f7426"/>
        </linearGradient>
        <linearGradient id="sliver" x1="0" y1="0" x2="1" y2="0">
          <stop offset="0" stop-color="#e3c865"/>
          <stop offset="1" stop-color="#b38430"/>
        </linearGradient>
      </defs>
      <polygon points="925,0 1124,0 1124,749 1000,749 590,530" fill="var(--navy)"/>
      <polygon points="517,495 631,480 597,534" fill="url(#sliver)"/>
      <polygon points="517,495 1011,749 396,749" fill="var(--gold)" stroke="var(--gold)" stroke-width="1.5"/>
      <circle cx="800" cy="337" r="192" fill="url(#ring)"/>
    </svg>

    <div class="live-badge">
      <div class="pill">
        <svg class="play" viewBox="0 0 40 40" aria-hidden="true">
          <circle cx="20" cy="20" r="18" fill="var(--white)" stroke="var(--gold)" stroke-width="3"/>
          <polygon points="15,11 29,20 15,29" fill="var(--gold)"/>
        </svg>
        LIVE
      </div>
      <div class="label">FREE WEBINAR</div>
    </div>

    <h1 class="title">Ways to Debut a Novel with Sparkle and Flair</h1>

    <div class="schedule">
      <div class="date">MARCH 15, 2023</div>
      <div class="time">7:00PM AEDT</div>
    </div>

    <div class="pitch">
      <p>Worried that the process of launching your book isn’t glamorous enough?</p>
      <p>Don’t Worry, this webinar has all the tips &amp; tricks<br>to help you glam up your book launch and make<br>it something people will remember.</p>
    </div>

    <div class="register-band">REGISTER @</div>
    <div class="register-url">www.quillmarket.com.au/webinars</div>

    <div class="brand">QUILL<br>MARKET</div>

    <div class="event-photo" role="img" aria-label="Group photo of smiling authors holding up their books at a launch event"></div>
  </section>
</div>
</body>
</html>
```